CALDERWYN STATIONARY
CALDRWYN STATIONARY
CALDERWYN STATIONARY -
Creative Brief
Professional
KHALID R AL-MUTAWA
CEO
P.O.BOX: 57384 RIYADH: 12958 KINGDOM OF SAUDI ARABIA
kalmutawa@mailvero.com
www.calderwyn-example.com

```html
<!DOCTYPE html>
<html lang="en">
<head>
<meta charset="utf-8">
<title>Calderwyn Business Card</title>
<link href="https://fonts.googleapis.com/css2?family=Open+Sans:wght@400;600;700&display=swap" rel="stylesheet">
<style>
  :root {
    --backdrop: #e9e6e1;
    --card: #ffffff;
    --gold: #c99a2e;
    --gold-light: #f1d27a;
    --gold-dark: #9c7216;
    --blue: #1f4f9c;
    --ink: #3b3b3b;
    --rule: #b9b9b9;
  }
  * { box-sizing: border-box; margin: 0; padding: 0; }
  html, body { width: 1200px; height: 852px; overflow: hidden; }
  body {
    background: var(--backdrop);
    font-family: "Open Sans", Arial, sans-serif;
    color: var(--ink);
    position: relative;
  }
  .card {
    position: absolute;
    width: 540px;
    height: 310px;
    background: var(--card);
    border-radius: 16px;
    overflow: hidden;
    box-shadow: 0 6px 18px rgba(0,0,0,.18);
  }
  .card--front { left: 90px; top: 110px; }
  .card--back { left: 570px; top: 440px; }
  .card__corners { position: absolute; inset: 0; }

  .brand { display: flex; align-items: center; gap: 10px; }
  .brand__mark {
    width: 34px; height: 34px;
    background: linear-gradient(135deg, var(--gold-light), var(--gold) 55%, var(--gold-dark));
  }
  .brand__name {
    font-weight: 600; font-size: 30px; letter-spacing: 1px; color: var(--gold);
  }
  .tagline {
    font-weight: 700; font-size: 10.5px; color: var(--blue); letter-spacing: .3px;
  }

  .person__name { font-weight: 700; font-size: 13px; color: var(--gold); letter-spacing: .3px; }
  .person__title { font-size: 11px; margin-top: 2px; }
  .address { font-size: 10px; line-height: 1.35; margin-top: 12px; }

  .contacts { list-style: none; font-size: 10px; line-height: 1.7; }
  .contacts li { display: flex; align-items: center; gap: 7px; }
  .contacts svg { width: 11px; height: 11px; flex: none; }

  .card--front .front__brand {
    position: absolute; left: 26px; top: 112px; width: 232px;
    display: flex; flex-direction: column; align-items: flex-start; gap: 6px;
  }
  .card--front .divider {
    position: absolute; left: 272px; top: 70px; width: 1px; height: 200px; background: var(--rule);
  }
  .card--front .front__info { position: absolute; left: 288px; top: 66px; }
  .card--front .contacts { margin-top: 12px; }

  .card--back .back__brand {
    position: absolute; left: 0; right: 0; top: 44px;
    display: flex; flex-direction: column; align-items: center; gap: 6px;
  }
  .card--back .back__person { position: absolute; left: 118px; top: 150px; }
  .card--back .divider {
    position: absolute; left: 284px; top: 150px; width: 1px; height: 118px; background: var(--rule);
  }
  .card--back .contacts { position: absolute; left: 298px; top: 146px; }
</style>
</head>
<body>

<svg width="0" height="0" style="position:absolute">
  <defs>
    <linearGradient id="goldBand" x1="0" y1="0" x2="1" y2="1">
      <stop offset="0" stop-color="#f3d884"/>
      <stop offset=".5" stop-color="#c99a2e"/>
      <stop offset="1" stop-color="#8f6712"/>
    </linearGradient>
    <symbol id="icon-phone" viewBox="0 0 12 12">
      <path d="M2.5 1 L4.5 1 L5.2 3.5 L4 4.5 Q5 7 7.5 8 L8.5 6.8 L11 7.5 L11 9.5 Q10 11 8 10.8 Q2 9.5 1.2 3.2 Q1 1.8 2.5 1Z" fill="#c99a2e"/>
    </symbol>
    <symbol id="icon-mobile" viewBox="0 0 12 12">
      <rect x="3" y="0.8" width="6" height="10.4" rx="1.2" fill="#c99a2e"/>
      <rect x="4" y="2" width="4" height="6.5" fill="#fff"/>
    </symbol>
    <symbol id="icon-mail" viewBox="0 0 12 12">
      <circle cx="6" cy="6" r="5.2" fill="none" stroke="#c99a2e" stroke-width="1.4"/>
      <circle cx="6" cy="6" r="2" fill="none" stroke="#c99a2e" stroke-width="1.4"/>
    </symbol>
    <symbol id="icon-web" viewBox="0 0 12 12">
      <circle cx="6" cy="6" r="5.2" fill="#c99a2e"/>
      <path d="M1 6 H11 M6 1 Q3 6 6 11 Q9 6 6 1" fill="none" stroke="#fff" stroke-width=".8"/>
    </symbol>
  </defs>
</svg>

<section class="card card--front" aria-label="Business card front">
  <svg class="card__corners" viewBox="0 0 540 310" preserveAspectRatio="none" aria-hidden="true">
    <path d="M360 0 Q470 8 540 110 L540 0 Z" fill="url(#goldBand)"/>
    <path d="M350 0 Q468 14 540 126" fill="none" stroke="var(--blue)" stroke-width="3"/>
    <path d="M0 190 Q60 292 190 310 L0 310 Z" fill="url(#goldBand)"/>
    <path d="M0 174 Q56 292 204 310" fill="none" stroke="var(--blue)" stroke-width="3"/>
  </svg>

  <div class="front__brand">
    <div class="brand">
      <div class="brand__mark"></div>
      <div class="brand__name">CALDERWYN</div>
    </div>
    <div class="tagline">STEADY GROWTH FOR EVERY PARTNER</div>
  </div>

  <div class="divider"></div>

  <div class="front__info">
    <div class="person__name">KHALID R AL-MUTAWA</div>
    <div class="person__title">CEO</div>
    <div class="address">P.O.BOX: 57384<br>RIYADH: 12958<br>KINGDOM OF SAUDI ARABIA</div>
    <ul class="contacts">
      <li><svg><use href="#icon-phone"/></svg>920004417</li>
      <li><svg><use href="#icon-phone"/></svg>+966 1 555 0143</li>
      <li><svg><use href="#icon-mobile"/></svg>+966 55 501 2276</li>
      <li><svg><use href="#icon-phone"/></svg>+966 1 555 0198</li>
      <li><svg><use href="#icon-mail"/></svg>kalmutawa@mailvero.com</li>
      <li><svg><use href="#icon-web"/></svg>www.calderwyn-example.com</li>
    </ul>
  </div>
</section>

<section class="card card--back" aria-label="Business card back">
  <svg class="card__corners" viewBox="0 0 540 310" preserveAspectRatio="none" aria-hidden="true">
    <path d="M380 0 Q480 6 540 80 L540 0 Z" fill="url(#goldBand)"/>
    <path d="M368 0 Q478 12 540 96" fill="none" stroke="var(--blue)" stroke-width="3"/>
    <path d="M0 210 Q50 296 170 310 L0 310 Z" fill="url(#goldBand)"/>
    <path d="M0 194 Q48 296 186 310" fill="none" stroke="var(--blue)" stroke-width="3"/>
  </svg>

  <div class="back__brand">
    <div class="brand">
      <div class="brand__mark"></div>
      <div class="brand__name">CALDERWYN</div>
    </div>
    <div class="tagline">STEADY GROWTH FOR EVERY PARTNER</div>
  </div>

  <div class="back__person">
    <div class="person__name">KHALID R AL-MUTAWA</div>
    <div class="person__title">CEO</div>
    <div class="address">P.O.BOX: 57384<br>RIYADH: 12958<br>KINGDOM OF SAUDI ARABIA</div>
  </div>

  <div class="divider"></div>

  <ul class="contacts">
    <li><svg><use href="#icon-phone"/></svg>920004417</li>
    <li><svg><use href="#icon-phone"/></svg>+966 1 555 0143</li>
    <li><svg><use href="#icon-mobile"/></svg>+966 55 501 2276</li>
    <li><svg><use href="#icon-phone"/></svg>+966 1 555 0198</li>
    <li><svg><use href="#icon-mail"/></svg>kalmutawa@mailvero.com</li>
    <li><svg><use href="#icon-web"/></svg>www.calderwyn-example.com</li>
  </ul>
</section>

</body>
</html>
```